Business Cards

We were billed for this because the project timed out. Please give me another designed to open this back up. I was not happy with the last designs (that I was charged for).
we are also using the logo with Clear Water Care Through Every Season
Also want to utilize Where Healthy Water is our Commitment.

Contact Information for Business Card

Marlowe Stone Group Inc

```html
<!DOCTYPE html>
<html lang="en">
<head>
<meta charset="UTF-8">
<title>Marlowe Stone Group — Business Cards</title>
<link href="https://fonts.googleapis.com/css2?family=Montserrat:wght@400;500;600;800&display=swap" rel="stylesheet">
<style>
  :root {
    --stage: #252526;
    --card: #1b1b1c;
    --brand-grey: #4a4a4c;
    --brand-grey-dim: #3a3a3c;
    --accent: #1a78c2;
    --text: #e8e8e8;
  }
  * { margin: 0; padding: 0; box-sizing: border-box; }
  html, body { width: 1200px; height: 900px; overflow: hidden; }
  body {
    background: var(--stage);
    font-family: "Montserrat", sans-serif;
    display: flex;
    flex-direction: column;
    align-items: center;
    justify-content: center;
    gap: 36px;
  }
  .card {
    position: relative;
    width: 700px;
    height: 400px;
    background: var(--card);
    border-radius: 26px;
    box-shadow: 0 18px 40px rgba(0,0,0,.55);
    overflow: hidden;
  }

  /* Front */
  .card--front { display: flex; align-items: center; justify-content: center; }
  .lockup__row { display: flex; align-items: center; gap: 16px; }
  .lockup__mark { width: 30px; height: 30px; background: var(--brand-grey); flex: none; }
  .lockup__name {
    font-weight: 800;
    font-size: 34px;
    letter-spacing: 2px;
    color: var(--brand-grey);
    text-transform: uppercase;
    white-space: nowrap;
  }
  .lockup__tagline {
    margin-top: 6px;
    margin-left: 46px;
    font-weight: 500;
    font-size: 12.5px;
    letter-spacing: 3.2px;
    color: var(--brand-grey-dim);
    text-transform: uppercase;
    white-space: nowrap;
  }

  /* Back */
  .back__brand { position: absolute; left: 44px; top: 48px; }
  .back__brand .brand-name {
    font-weight: 800; font-size: 21px; letter-spacing: 1.6px;
    color: var(--brand-grey); text-transform: uppercase; white-space: nowrap;
  }
  .back__brand .brand-tagline {
    margin-top: 3px; font-weight: 500; font-size: 8.5px; letter-spacing: 2.2px;
    color: var(--brand-grey-dim); text-transform: uppercase; white-space: nowrap;
  }
  .person { position: absolute; right: 50px; top: 44px; text-align: right; }
  .person__name { font-weight: 600; font-size: 26px; color: var(--accent); white-space: nowrap; }
  .person__role { font-size: 13px; color: var(--text); margin-top: 2px; }
  .accent-bar {
    position: absolute; right: 0; top: 40px;
    width: 12px; height: 40px; background: var(--accent);
  }
  .address {
    position: absolute; left: 50px; bottom: 150px;
    font-size: 16px; line-height: 1.3; color: var(--text);
  }
  .contacts {
    position: absolute; left: 50px; bottom: 48px;
    list-style: none; font-size: 16px; color: var(--text);
  }
  .contacts li { display: flex; align-items: center; gap: 12px; line-height: 27px; white-space: nowrap; }
  .contacts svg { width: 15px; height: 15px; fill: var(--accent); flex: none; }
  .back__wordmark {
    position: absolute; right: 50px; bottom: 92px;
    display: flex; align-items: center; gap: 12px;
  }
  .back__wordmark .mark { width: 34px; height: 34px; background: var(--brand-grey); flex: none; }
  .back__wordmark .brand-name {
    font-weight: 800; font-size: 36px; letter-spacing: 2px;
    color: var(--brand-grey); text-transform: uppercase; line-height: 1;
  }
</style>
</head>
<body>

  <section class="card card--front" aria-label="Card front">
    <div class="lockup">
      <div class="lockup__row">
        <span class="lockup__mark"></span>
        <span class="lockup__name">Marlowe Stone Group</span>
      </div>
      <p class="lockup__tagline">Clear Water Care Through Every Season</p>
    </div>
  </section>

  <section class="card card--back" aria-label="Card back">
    <div class="back__brand">
      <p class="brand-name">Marlowe Stone Group</p>
      <p class="brand-tagline">Clear Water Care Through Every Season</p>
    </div>

    <div class="person">
      <p class="person__name">Dana Whitfield</p>
      <p class="person__role">owner</p>
    </div>
    <span class="accent-bar"></span>

    <p class="address">418 Linden Park Ave, #112<br>Fairhaven, OH 43190</p>

    <ul class="contacts">
      <li>
        <svg viewBox="0 0 16 16" aria-hidden="true"><path d="M3.5 1h3l1 3.5-2 1.3a9 9 0 0 0 4.7 4.7l1.3-2 3.5 1v3a1.5 1.5 0 0 1-1.5 1.5A12.5 12.5 0 0 1 2 2.5 1.5 1.5 0 0 1 3.5 1z"/></svg>
        555-014-2736
      </li>
      <li>
        <svg viewBox="0 0 16 16" aria-hidden="true"><path d="M8 1a7 7 0 1 0 0 14A7 7 0 0 0 8 1zm0 1.6c.9 0 1.9 1.9 2.2 4.6H5.8C6.1 4.5 7.1 2.6 8 2.6zM2.7 8.8h1.6c.1 1.6.5 3 1 4A5.5 5.5 0 0 1 2.7 8.8zm0-1.6a5.5 5.5 0 0 1 2.6-4c-.5 1-.9 2.4-1 4H2.7zM8 13.4c-.9 0-1.9-1.9-2.2-4.6h4.4c-.3 2.7-1.3 4.6-2.2 4.6zm2.7-.6c.5-1 .9-2.4 1-4h1.6a5.5 5.5 0 0 1-2.6 4zm1-5.6c-.1-1.6-.5-3-1-4a5.5 5.5 0 0 1 2.6 4h-1.6z"/></svg>
        info@marlowestonegroup.com
      </li>
      <li>
        <svg viewBox="0 0 16 16" aria-hidden="true"><path d="M1 3.5h14v1.2L8 9 1 4.7z"/><path d="M1 6.2l7 4.3 7-4.3v6.3H1z"/></svg>
        www.marlowestonegroup.com
      </li>
    </ul>

    <div class="back__wordmark">
      <span class="mark"></span>
      <span class="brand-name">Marlowe<br>Stone</span>
    </div>
  </section>

</body>
</html>
```